Business Card Design Project

Marla's Elixirs is a natural skincare business and we need a business card designed. The company focuses on natural products and will be launching with body scrubs and bath fizzies and our mission statement is: To deliver high quality natural beauty products at a good value. It's two cards - one design - the only information changing would be name and email address

Target Market(s)

Females ages 20-50

Industry/Entity Type

Business

Requirements
Must have
• Marla's Elixirs

Yvonne Hart-Becker
T: 800-555-7341
E: Yvonne@MarlasElixirs-example.com
W: www.MarlasElixirs-example.com

Tobias Werner
T: 800-555-7341
E: Tobias@MarlasElixirs-example.com
W: www.MarlasElixirs-example.com
Nice to have
• I'd like to use the colors or text found at www.marlaselixirs-example.com but I'm open to suggestions since design isn't set in stone yet. I would also like to have the words .....a little bit of magic somewhere under the company name in a different type of font. I would like a design that feels clean and maybe a retro feel to it - front and back would be nice but not mandatory

```html
<!DOCTYPE html>
<html lang="en">
<head>
<meta charset="utf-8">
<title>Marla's Elixirs – Business Cards</title>
<link rel="stylesheet" href="https://fonts.googleapis.com/css2?family=Source+Sans+3:ital,wght@0,400;0,600;0,700;1,400&display=swap">
<style>
  :root {
    --backdrop: #eee4d3;
    --card-white: #ffffff;
    --card-cream: #fbfbe6;
    --card-yellow: #f1ee8c;
    --water-light: #8fd3ec;
    --water-mid: #36b0dc;
    --water-deep: #1a95cb;
    --brand-purple: #7a2c8c;
    --band-blue-start: #19a9de;
    --band-blue-end: #bfe6f7;
    --ink: #222222;
    --icon-frame: #1f1f1f;
  }
  * { box-sizing: border-box; margin: 0; padding: 0; }
  html, body {
    width: 1200px;
    height: 900px;
    overflow: hidden;
    background: var(--backdrop);
    font-family: "Source Sans 3", Arial, sans-serif;
  }
  .card-sheet {
    position: relative;
    width: 1200px;
    height: 900px;
  }
  .business-card {
    position: absolute;
    left: 316px;
    width: 616px;
    height: 354px;
    overflow: hidden;
    background: linear-gradient(100deg, var(--card-white) 0%, var(--card-cream) 45%, var(--card-yellow) 100%);
    box-shadow: 0 2px 6px rgba(0,0,0,0.18);
  }
  .business-card--first { top: 66px; }
  .business-card--second { top: 486px; }
  .water-panel {
    position: absolute;
    inset: 0;
    width: 616px;
    height: 354px;
  }
  .brand {
    position: absolute;
    left: 24px;
    top: 22px;
    display: flex;
    align-items: center;
  }
  .brand-name {
    font-weight: 600;
    font-size: 40px;
    line-height: 1;
    color: var(--brand-purple);
    letter-spacing: 0.5px;
  }
  .brand-mark {
    width: 10px;
    height: 10px;
    border-radius: 50%;
    background: var(--brand-purple);
    margin-left: 8px;
    margin-top: 10px;
  }
  .name-band {
    position: absolute;
    left: 0;
    top: 120px;
    width: 310px;
    height: 40px;
    border-radius: 0 14px 14px 0;
    background: linear-gradient(90deg, var(--band-blue-start) 0%, var(--band-blue-end) 100%);
  }
  .person-name {
    position: absolute;
    left: 40px;
    top: 6px;
    font-weight: 700;
    font-size: 23px;
    color: var(--brand-purple);
    white-space: nowrap;
  }
  .contact-list {
    position: absolute;
    left: 40px;
    top: 190px;
    list-style: none;
  }
  .contact-item {
    display: flex;
    align-items: center;
    height: 42px;
    font-style: italic;
    font-size: 19px;
    color: var(--ink);
    white-space: nowrap;
  }
  .contact-icon {
    width: 26px;
    height: 26px;
    margin-right: 20px;
    flex: none;
  }
</style>
</head>
<body>
<main class="card-sheet">

  <section class="business-card business-card--first">
    <svg class="water-panel" viewBox="0 0 616 354" role="img" aria-label="Blue water surface with droplets">
      <defs>
        <linearGradient id="waterFillA" x1="0" y1="0" x2="1" y2="1">
          <stop offset="0" stop-color="var(--water-light)"/>
          <stop offset="0.55" stop-color="var(--water-mid)"/>
          <stop offset="1" stop-color="var(--water-deep)"/>
        </linearGradient>
      </defs>
      <path d="M224 354 Q 520 300 612 20 L616 20 L616 354 Z" fill="#ffffff"/>
      <path d="M238 354 Q 528 304 616 34 L616 354 Z" fill="url(#waterFillA)"/>
    </svg>
    <div class="brand">
      <span class="brand-name">Marla's Elixirs</span><span class="brand-mark"></span>
    </div>
    <div class="name-band"><span class="person-name">Yvonne Hart-Becker</span></div>
    <ul class="contact-list">
      <li class="contact-item">
        <svg class="contact-icon" viewBox="0 0 26 26" aria-hidden="true"><rect x="1" y="1" width="24" height="24" rx="4" fill="none" stroke="var(--icon-frame)" stroke-width="2"/><path d="M8 6 l3 0 l1 4 l-2 1.5 q1.5 3.5 4.5 4.5 l1.5 -2 l4 1 l0 3 q-8 1 -12 -12 z" fill="var(--icon-frame)"/></svg>
        <span>800-555-7341</span>
      </li>
      <li class="contact-item">
        <svg class="contact-icon" viewBox="0 0 26 26" aria-hidden="true"><rect x="1" y="1" width="24" height="24" rx="4" fill="none" stroke="var(--icon-frame)" stroke-width="2"/><rect x="6" y="8" width="14" height="10" fill="none" stroke="var(--icon-frame)" stroke-width="1.6"/><path d="M6 8 l7 6 l7 -6" fill="none" stroke="var(--icon-frame)" stroke-width="1.6"/></svg>
        <span>Yvonne@MarlasElixirs-example.com</span>
      </li>
      <li class="contact-item">
        <svg class="contact-icon" viewBox="0 0 26 26" aria-hidden="true"><rect x="1" y="1" width="24" height="24" rx="4" fill="none" stroke="var(--icon-frame)" stroke-width="2"/><rect x="6" y="7" width="14" height="10" fill="var(--icon-frame)"/><rect x="10" y="18" width="6" height="2" fill="var(--icon-frame)"/></svg>
        <span>www.MarlasElixirs-example.com</span>
      </li>
    </ul>
  </section>

  <section class="business-card business-card--second">
    <svg class="water-panel" viewBox="0 0 616 354" role="img" aria-label="Blue water surface with droplets">
      <defs>
        <linearGradient id="waterFillB" x1="0" y1="0" x2="1" y2="1">
          <stop offset="0" stop-color="var(--water-light)"/>
          <stop offset="0.55" stop-color="var(--water-mid)"/>
          <stop offset="1" stop-color="var(--water-deep)"/>
        </linearGradient>
      </defs>
      <path d="M224 354 Q 520 300 612 20 L616 20 L616 354 Z" fill="#ffffff"/>
      <path d="M238 354 Q 528 304 616 34 L616 354 Z" fill="url(#waterFillB)"/>
    </svg>
    <div class="brand">
      <span class="brand-name">Marla's Elixirs</span><span class="brand-mark"></span>
    </div>
    <div class="name-band"><span class="person-name">Tobias Werner</span></div>
    <ul class="contact-list">
      <li class="contact-item">
        <svg class="contact-icon" viewBox="0 0 26 26" aria-hidden="true"><rect x="1" y="1" width="24" height="24" rx="4" fill="none" stroke="var(--icon-frame)" stroke-width="2"/><path d="M8 6 l3 0 l1 4 l-2 1.5 q1.5 3.5 4.5 4.5 l1.5 -2 l4 1 l0 3 q-8 1 -12 -12 z" fill="var(--icon-frame)"/></svg>
        <span>800-555-7341</span>
      </li>
      <li class="contact-item">
        <svg class="contact-icon" viewBox="0 0 26 26" aria-hidden="true"><rect x="1" y="1" width="24" height="24" rx="4" fill="none" stroke="var(--icon-frame)" stroke-width="2"/><rect x="6" y="8" width="14" height="10" fill="none" stroke="var(--icon-frame)" stroke-width="1.6"/><path d="M6 8 l7 6 l7 -6" fill="none" stroke="var(--icon-frame)" stroke-width="1.6"/></svg>
        <span>Tobias@MarlasElixirs-example.com</span>
      </li>
      <li class="contact-item">
        <svg class="contact-icon" viewBox="0 0 26 26" aria-hidden="true"><rect x="1" y="1" width="24" height="24" rx="4" fill="none" stroke="var(--icon-frame)" stroke-width="2"/><rect x="6" y="7" width="14" height="10" fill="var(--icon-frame)"/><rect x="10" y="18" width="6" height="2" fill="var(--icon-frame)"/></svg>
        <span>www.MarlasElixirs-example.com</span>
      </li>
    </ul>
  </section>

</main>
</body>
</html>
```